After tattoo calming solution

The label has to be modern, along the same lines as skin care brand “Plain Form.” It has to reflect the solutions natural effectiveness and simplicity. The label cannot be over fussy, and must be a little bit clinical, as it really does work. The colours should reflect that the solution calms the skin.

We use a 100ml spray bottle.

Target Market(s)

Anyone with a new tattoo or piercing

Industry/Entity Type

Skincare

Requirements
Must have
• Must reflect its natural calming but still remain a little clinical
Should not have
• It must not look like other flowery tattoo cream solutions.

```html
<!DOCTYPE html>
<html lang="en">
<head>
<meta charset="UTF-8">
<title>Settle Serum For Ink — Calming Solution Label</title>
<link href="https://fonts.googleapis.com/css2?family=Montserrat:wght@500;600;800&display=swap" rel="stylesheet">
<style>
  :root {
    --backdrop: #d3d3d3;
    --label: #e4e4e4;
    --teal: #4b9e9c;
    --ink: #0d0d0d;
  }
  html, body {
    margin: 0;
    padding: 0;
    width: 1200px;
    height: 1200px;
    overflow: hidden;
    background: var(--backdrop);
    font-family: "Montserrat", Arial, sans-serif;
  }
  .canvas {
    position: relative;
    width: 1200px;
    height: 1200px;
  }
  .label {
    position: absolute;
    left: 440px;
    top: 30px;
    width: 320px;
    height: 1140px;
    background: var(--label);
    overflow: hidden;
  }
  .headline {
    position: absolute;
    left: 30px;
    top: 108px;
    margin: 0;
    color: var(--teal);
    font-weight: 600;
    font-size: 47px;
    line-height: 40px;
    letter-spacing: 0.2px;
    white-space: nowrap;
  }
  .benefit {
    position: absolute;
    left: 28px;
    top: 328px;
    margin: 0;
    color: var(--ink);
    font-weight: 500;
    font-size: 19.5px;
    line-height: 21.5px;
    white-space: nowrap;
  }
  .product-name {
    position: absolute;
    left: 30px;
    top: 672px;
    margin: 0;
    color: var(--ink);
    font-weight: 800;
    font-size: 30px;
    line-height: 31px;
    white-space: nowrap;
  }
  .volume {
    position: absolute;
    left: 29px;
    top: 1012px;
    margin: 0;
    color: var(--ink);
    font-weight: 500;
    font-size: 18px;
  }
</style>
</head>
<body>
  <main class="canvas">
    <section class="label">
      <h1 class="headline">Clear<br>Calm<br>For New<br>Tattoos<br>&amp; Piercings</h1>
      <p class="benefit">Reduces Inflammation<br>Irritation and Encourages<br>Natural Skin Healing</p>
      <h2 class="product-name">SETTLE SERUM<br>FOR INK</h2>
      <p class="volume">100ML</p>
    </section>
  </main>
</body>
</html>
```